<作成物>
■リッチメッセージ
リッチメニュー
合計2枚

【デザインの詳細】
デザインの詳細イメージをファイルに入れております。
また、別の業種の方ですが、サンプルデザインをファイルのリンク先に付けておりますのでご確認ください。
上下で一体感があるものを希望します。

〈リッチメニューの表示項目〉
左上から① ホームページ・SNS・自己紹介 ②サービス紹介 ③動画で体験
左下から④オンラインショップ ⑤お客様の声 ⑥お問い合わせ

デザイン重視でここの表示名はデザイン的に英語の方がよければ
英語でも大丈夫です。意味がわかって
ニュアンスがあっていれば文字を短くするのも
お任せします。あくまでデザイン重視です。
〈画像はこちらから〉
素材画像
https://7.kumobako.example/3081-a4f2c9e7b1d05e6f38c2a9d4e7b61f05

※こちらの作成以外に勝手に使用された場合は
著作権侵害で法的手段をとらせていただきます。
作成事例にもしようしないでください。

<サイズ>
・リッチメッセージ(1040×1040ピクセル)
・リッチメニュー(1200×810ピクセル)

<納品形式>
・ai形式(イラストレーターデータ)
・psd形式(フォトショップデータ)
・JPG
<詳細>
※添付ファイルをご確認ください。

<備考>
ブランディング効果を期待しています。
どんどん何個でも応募ください。

```html
<!DOCTYPE html>
<html lang="ja">
<head>
<meta charset="utf-8">
<title>SORANE リッチメニュー</title>
<link rel="stylesheet" href="https://fonts.googleapis.com/css2?family=Noto+Serif+JP:wght@400;500&family=Noto+Sans+JP:wght@400&display=swap">
<style>
  :root{
    --sky-top:#8a7e6c;
    --sky-mid:#c9a56a;
    --horizon:#f1d79a;
    --sea-mid:#a9824c;
    --sea-deep:#4e3a22;
    --text-light:#ffffff;
    --text-dark:#4a3a2c;
    --label-bg:rgba(255,250,240,0.55);
  }
  *{margin:0;padding:0;box-sizing:border-box}
  html,body{width:716px;height:1200px;overflow:hidden;background:#fff}
  .canvas{position:relative;width:716px;height:1200px;overflow:hidden}

  .hero{position:absolute;left:0;top:0;width:716px;height:490px;
    background:linear-gradient(180deg,var(--sky-top) 0%,var(--sky-mid) 12%,var(--horizon) 24%,#d9b274 32%,var(--sea-mid) 48%,#7d5c34 66%,#a8814c 78%,var(--sea-deep) 100%);}
  .brand{position:absolute;left:48px;top:78px;display:flex;align-items:center;gap:12px;
    color:var(--text-light);font-family:"Noto Serif JP",serif;font-weight:400;
    font-size:34px;letter-spacing:6px;line-height:1}
  .brand-dot{width:12px;height:12px;border-radius:50%;background:var(--text-light)}
  .tagline{position:absolute;left:0;top:0;width:716px;height:490px;
    font-family:"Noto Serif JP",serif;font-weight:500;font-size:22px;color:var(--text-light);
    text-shadow:0 1px 3px rgba(60,35,10,0.6)}
  .tagline span{position:absolute;white-space:nowrap}

  .photo-strip{position:absolute;left:0;top:490px;width:716px;height:222px}
  .photo{position:absolute;top:0;height:222px}
  .photo-a{left:0;width:358px;background:linear-gradient(120deg,#3c5d5c 0%,#b07548 35%,#d9a070 55%,#4c3a2a 100%)}
  .photo-b{left:360px;width:183px;background:linear-gradient(160deg,#8a5a36 0%,#c58a5e 50%,#3e2c20 100%)}
  .photo-c{left:545px;width:171px;background:linear-gradient(180deg,#e9e6e2 0%,#d7cfc6 55%,#9c8a78 100%)}

  .menu{position:absolute;left:0;top:712px;width:716px;height:488px}
  .tile{position:absolute;width:238px;height:243px;overflow:hidden}
  .tile-bg{position:absolute;inset:0}
  .label{position:absolute;left:24px;top:32px;width:184px;height:182px;background:var(--label-bg);
    font-family:"Noto Serif JP",serif;font-weight:400;font-size:25px;line-height:1.3;color:var(--text-dark);
    display:flex;align-items:flex-end;padding:0 0 14px 12px}
  .t1{left:0;top:0}.t2{left:239px;top:0}.t3{left:478px;top:0}
  .t4{left:0;top:245px}.t5{left:239px;top:245px}.t6{left:478px;top:245px}
  .t1 .tile-bg{background:linear-gradient(135deg,#7a5538,#c99a78 50%,#5a3e2c)}
  .t2 .tile-bg{background:linear-gradient(135deg,#d9b79a,#a87854 50%,#5e4230)}
  .t3 .tile-bg{background:radial-gradient(circle at 60% 55%,#e6f4f2 0%,#8cc7c4 40%,#3f8a8a 100%)}
  .t4 .tile-bg{background:linear-gradient(180deg,#9aa2ac 0%,#e8cf9a 45%,#c2a476 60%,#5c5a54 100%)}
  .t5 .tile-bg{background:linear-gradient(150deg,#5aa6a8 0%,#bfe0dc 45%,#d9b77a 75%,#7a6446 100%)}
  .t6 .tile-bg{background:linear-gradient(135deg,#3a2a1e,#b48462 50%,#e2c29a)}
</style>
</head>
<body>
<main class="canvas">
  <section class="hero" role="img" aria-label="夕日に染まる黄金色の海の写真">
    <div class="brand"><span class="brand-dot"></span><span class="brand-name">SORANE</span></div>
    <p class="tagline">
      <span style="left:248px;top:284px">正の周波数と共振することで</span>
      <span style="right:18px;top:326px">思考や感情脳内がクリアに。</span>
      <span style="left:248px;top:372px">世界で唯一の『癒しの音』と『エステ』で、</span>
      <span style="left:248px;top:420px">他にはない極上の癒しをご堪能下さい。</span>
    </p>
  </section>

  <section class="photo-strip">
    <div class="photo photo-a" role="img" aria-label="背中のオイルマッサージの写真"></div>
    <div class="photo photo-b" role="img" aria-label="施術中のマッサージの写真"></div>
    <div class="photo photo-c" role="img" aria-label="シンギングボウルが置かれた明るい施術室の写真"></div>
  </section>

  <nav class="menu">
    <a class="tile t1"><div class="tile-bg" role="img" aria-label="エステ施術の写真"></div><span class="label">HP<br>SNS<br>自己紹介</span></a>
    <a class="tile t2"><div class="tile-bg" role="img" aria-label="マッサージ施術の写真"></div><span class="label">サービス<br>紹介</span></a>
    <a class="tile t3"><div class="tile-bg" role="img" aria-label="水面の波紋の写真"></div><span class="label">動画で<br>体験</span></a>
    <a class="tile t4"><div class="tile-bg" role="img" aria-label="夕暮れの海辺の写真"></div><span class="label">オンライン<br>ショップ</span></a>
    <a class="tile t5"><div class="tile-bg" role="img" aria-label="水辺と花の写真"></div><span class="label">お客様の声</span></a>
    <a class="tile t6"><div class="tile-bg" role="img" aria-label="手のひらに触れる施術の写真"></div><span class="label">お問い合わせ</span></a>
  </nav>
</main>
</body>
</html>
```